Coaching Business Needs a Website

Business Name: Bright Orbit Coaching
My Name: Martin Hollowbrook

I am a human behaviour expert that needs not just a website, but in the process a "personality" for my brand (Bright Orbit).

With your brilliance and creativity, I want my reputation to be the go to expert in changing unresourceful human behaviour (eg. smoking, eating sugar, procrastination, overwhelm, fear, laziness, weight-gain, phobias, lack of motivation, etc).

===========================
Page 1 (Titled: 'Start Here')

My tag line is "Bright Orbit". The home page should be friendly, inviting, exciting, empowering, positive and innovative.

My Mission Quote: (so people know why I do what I do)

"Our mission is to improve as many people's lives as we can, when we can, through workshops, being guest speaker at events, coaching/mentoring and with valuable products." - Martin Hollowbrook, Human Behaviour Expert (I will give you a photo of me to put with this quote).

My marketing strategy is to share how I ride, because that is my focus (the experience that clients get). Please show the following on my Page 1:

- My mission quote (see above).
- A video (please insert any video at this stage, as I will get a marketing video professionally made to go on this page 1 of my website).
- 10 Reasons Why People Choose 'Bright Orbit Coaching'.
- What We Offer (with Call To Action Buttons, see below).
- Success Stories (these are our Testimonials).

-------------------------------------------
10 Reasons Why People Choose 'Bright Orbit Coaching':

Reason No. 1 We know how to make Bright Orbit in other people's lives. This is our favourite method of making change.

Reason No. 2 We give away a lot of FREE stuff.

Reason No. 3 We thank you for accepting FREE stuff. We are genuinely grateful for you accepting our FREE stuff.

Reason No. 4 We give you a feeling of belonging.

Reason No. 5 We give you the feeling that you are special, because you are.

Reason No. 6 We give you the feeling of significance, because you deserve it.

Reason No. 7 We give you the feeling of feeling good.

Reason No. 8 We give you positive, empowering experiences.

Reason No. 9 We give you tools, models and methodologies to improve every area of your life, continuously for the rest of your life. You can have fulfillment.

Reason No. 10 We give you value beyond what you can imagine.

What We Offer: (each of the following with a picture and more details)

1. Personal Coaching / Mentoring (more details: 1st Session FREE, valued at A$125, Unlimited chat support, call to action button to go to https://bookwell.example/brightorbitcoaching).

2. Human Behaviour Events (more details: next upcoming event, call to action button to go to... I will provide later.. I want to be able to change this hyperlink regularly to the latest upcoming event).

3. Guest Speaker / Master of Ceremonies (call to action button to go to 'Contact Us' website page).

4. Great Value Products (call to action button to go to 'Products' website page).

5. Great FREE Information (call to action button to go to 'Blogs' website page).

Success Stories:

Please allow for 10 written testimonial stories to be added. Please put 10 random text ones so I know what it will look like. I want to be able to change the text in the future. It would be good to put the person's picture and a star rating (eg. 5 stars).

Page 2 (Title: 'Products')

A place where I can add products...

Page 3 (Titled: 'Blogs')

A place where I can add written blogs...

Page 4 (Titled: 'Contact Us')

Contact us form with:
- Name
- Email Address
- Contact Number
- Message

Thank you. I look forward to working with you!!! I will upload my Logo for you to use.

Target Market(s)

Real, Everyday People - Men & Women aged between 21 - 50, who want to change several behaviours in their health, career, relationship, etc, that they feel are holding them back.

Industry/Entity Type

Life Coaching

Contact Information for Business Card

My Name: Martin Hollowbrook, Bright Orbit Expert
Mobile: xxxxxxxxxxxxxx
Email: xxxxxxxxxxxxxx@mailbox.example
Website: brightorbitcoaching.example.au

On the back have what we do:
1. Personal Coaching / Mentoring
2. Human Behaviour Events
3. Guest Speaker / Master of Ceremonies

Coding

Coded - Design and coding required

Number of Pages Required

4 page

Colors
ffc214

Requirements
Must have
• Inspiring images... My website must come across as fun, social, happy, and inviting. The website must have a personality; it is a marketing lead generation tool. It must represent Martin Hollowbrook as being a Human Behaviour Expert (ie. video & testimonials) and must have Call To Action buttons. The website should look professional, not something done using a cheap template. The colour selected is GOLD.
Nice to have
• Additional creative functionality...
Should not have
• It should not have anything negative on it.

```html
<!DOCTYPE html>
<html lang="en">
<head>
<meta charset="utf-8">
<title>Bright Orbit Coaching — Start Here</title>
<link rel="stylesheet" href="https://fonts.googleapis.com/css2?family=Source+Sans+3:wght@300;400;600;700&display=swap">
<style>
:root{
  --gold:#ffc214;
  --gold-light:#ffd85a;
  --ink:#1f2124;
  --charcoal:#2b2c2e;
  --footer:#25272a;
  --white:#ffffff;
  --text:#333333;
  --muted:#8a8a8a;
  --hero-a:#cfd3d6;
  --hero-b:#8b8f92;
}
*{margin:0;padding:0;box-sizing:border-box}
html,body{width:864px;height:1200px;overflow:hidden;background:var(--white)}
body{position:relative;font-family:"Source Sans 3",Arial,sans-serif;color:var(--text)}
.abs{position:absolute}

/* header */
.site-header{left:0;top:0;width:864px;height:89px;background:var(--ink)}
.brand{left:102px;top:26px;display:flex;align-items:center;gap:10px}
.brand-dot{width:34px;height:34px;border-radius:50%;background:var(--gold)}
.brand-name{color:var(--gold);font-weight:600;font-size:20px;line-height:1}
.phone{right:104px;top:24px;color:var(--white);font-size:13px;display:flex;align-items:center;gap:5px}
.main-nav{right:104px;top:47px;display:flex;gap:18px}
.main-nav a{color:var(--white);text-decoration:none;font-size:13px;padding-bottom:3px}
.main-nav a.active{border-bottom:2px solid var(--gold)}

/* hero */
.hero{left:0;top:89px;width:864px;height:302px;background:linear-gradient(100deg,var(--hero-a),#b9bdc0 45%,var(--hero-b) 70%,#e1e4e6)}

/* mission */
.mission{left:0;top:391px;width:864px;height:183px;background:var(--ink);overflow:hidden}
.mission-accent{left:0;top:0}
.founder-photo{left:104px;top:40px;width:106px;height:106px;border-radius:50%;background:radial-gradient(circle at 50% 40%,#7b8a7a,#34473c)}
.mission-title{left:227px;top:28px;color:var(--white);font-weight:300;font-size:27px}
.mission-quote{left:229px;top:68px;width:210px;color:var(--white);font-size:9px;line-height:1.2}
.founder-name{left:229px;top:122px;color:var(--gold);font-size:14px}
.founder-role{left:229px;top:141px;color:var(--white);font-size:8.5px}
.video{left:490px;top:17px;width:269px;height:150px;background:#000}
.video-bar{left:0;bottom:0;width:269px;height:16px;background:#f2f2f2;display:flex;align-items:center;gap:5px;padding:0 6px}
.video-track{flex:1;height:3px;background:#333}
.video-time{background:#222;color:#fff;font-size:6px;padding:1px 3px;border-radius:2px}
.video-vol{width:28px;height:3px;background:#333}

/* reasons */
.reasons-title{left:102px;top:594px;font-weight:300;font-size:26px;color:var(--ink)}
.reasons-title strong{font-weight:600}
.reasons-list{left:106px;top:637px;list-style:none}
.reasons-list li{display:flex;align-items:center;gap:9px;height:16.8px;font-size:8.6px;color:var(--ink)}
.reasons-list li::before{content:"";width:8px;height:8px;border-radius:50%;background:var(--ink);flex:none;
  background-image:linear-gradient(45deg,transparent 44%,#fff 44%,#fff 56%,transparent 56%);}

/* lower */
.lower{left:0;top:826px;width:864px;height:326px;background:var(--charcoal)}
.section-title{color:var(--white);font-weight:300;font-size:26px;top:26px}
.stories{left:104px;top:73px;display:grid;grid-template-columns:177px 177px;row-gap:11px}
.story{display:flex;gap:10px;height:35px}
.story-photo{width:35px;height:35px;background:linear-gradient(#7a8470,#3e4a40);flex:none}
.story-name{color:var(--gold);font-size:9px;line-height:1}
.story-text{color:var(--white);font-size:6.8px;margin-top:3px}
.stars{display:flex;gap:3px;margin-top:3px}
.offers{left:448px;top:72px;display:flex;flex-direction:column;gap:8.6px}
.offer{position:relative;width:302px;height:38px;background:linear-gradient(#ffd24a,var(--gold));display:flex;align-items:center;gap:9px;padding-left:14px;text-decoration:none;color:var(--ink);font-weight:700;font-size:11.5px;overflow:hidden}
.offer svg.chev{position:absolute;right:0;top:0}

/* footer */
.site-footer{left:0;top:1152px;width:864px;height:48px;background:var(--footer);border-top:1px solid #555}
.copyright{width:100%;text-align:center;margin-top:20px;font-size:8.5px;color:var(--muted)}
</style>
</head>
<body>

<header class="site-header abs">
  <div class="brand abs"><span class="brand-dot"></span><span class="brand-name">Bright Orbit Coaching</span></div>
  <div class="phone abs">
    <svg width="13" height="13" viewBox="0 0 24 24" fill="none" stroke="#ffc214" stroke-width="2"><path d="M5 3h4l2 5-3 2a12 12 0 0 0 6 6l2-3 5 2v4a2 2 0 0 1-2 2A18 18 0 0 1 3 5a2 2 0 0 1 2-2z"/></svg>
    Call Us-800-555-0147
  </div>
  <nav class="main-nav abs">
    <a class="active" href="#">Home</a><a href="#">Products</a><a href="#">Blog</a><a href="#">Contact Us</a>
  </nav>
</header>

<section class="hero abs" role="img" aria-label="Photo of two colleagues working together at a computer in a bright office"></section>

<section class="mission abs">
  <svg class="mission-accent abs" width="864" height="183"><polygon points="488,0 864,0 864,183 410,183" fill="#ffc214"/></svg>
  <div class="founder-photo abs" role="img" aria-label="Portrait of Martin Hollowbrook outdoors"></div>
  <h2 class="mission-title abs">Our Mission</h2>
  <p class="mission-quote abs">“Our mission is to improve as many people's lives as we can, when we can, through workshops, being guest speaker at events, coaching/mentoring and with valuable products.”</p>
  <div class="founder-name abs">Martin Hollowbrook</div>
  <div class="founder-role abs">Human Behaviour Expert</div>
  <div class="video abs">
    <svg class="abs" style="left:126px;top:58px" width="18" height="18" viewBox="0 0 18 18" stroke="#ccc" stroke-width="1.6" stroke-linecap="round">
      <path d="M9 1v4M9 13v4M1 9h4M13 9h4M3.3 3.3l2.8 2.8M11.9 11.9l2.8 2.8M3.3 14.7l2.8-2.8M11.9 6.1l2.8-2.8"/>
    </svg>
    <div class="video-bar abs">
      <svg width="7" height="8"><polygon points="0,0 7,4 0,8" fill="#222"/></svg>
      <div class="video-track"></div>
      <span class="video-time">00:00/03:48</span>
      <div class="video-vol"></div>
      <svg width="8" height="8"><rect x=".5" y=".5" width="7" height="7" fill="none" stroke="#222"/></svg>
    </div>
  </div>
</section>

<h2 class="reasons-title abs">10 Reasons Why People Choose <strong>Bright Orbit Coaching</strong></h2>
<ul class="reasons-list abs">
  <li>We know how to make Bright Orbit in other people's lives. This is our favourite method of making change.</li>
  <li>We give away a lot of FREE stuff.</li>
  <li>We thank you for accepting FREE stuff. We are genuinely grateful for you accepting our FREE stuff.</li>
  <li>We give you a feeling of belonging.</li>
  <li>We give you the feeling that you are special, because you are.</li>
  <li>We give you the feeling of significance, because you deserve it.</li>
  <li>We give you the feeling of feeling good.</li>
  <li>We give you positive, empowering experiences.</li>
  <li>We give you tools, models and methodologies to improve every area of your life, continuously for the rest of your life. You can have fulfillment.</li>
  <li>We give you value beyond what you can imagine.</li>
</ul>

<section class="lower abs">
  <h2 class="section-title abs" style="left:102px">Success Stories</h2>
  <h2 class="section-title abs" style="left:445px">What We Offer</h2>

  <div class="stories abs">
    <!-- ten testimonial slots -->
    <div class="story"><div class="story-photo" role="img" aria-label="Client photo"></div><div><div class="story-name">Martin Hollowbrook</div><div class="story-text">We have an exceptionally high</div><div class="stars"><svg width="60" height="9"><g fill="#ffc214"><path id="s" d="M4.5 0l1.3 2.9 3.2.3-2.4 2.1.7 3.1-2.8-1.6-2.8 1.6.7-3.1L0 3.2l3.2-.3z"/><use href="#s" x="12.5"/><use href="#s" x="25"/></g><g fill="#fff"><use href="#s" x="37.5"/><use href="#s" x="50"/></g></svg></div></div></div>
    <div class="story"><div class="story-photo" role="img" aria-label="Client photo"></div><div><div class="story-name">Martin Hollowbrook</div><div class="story-text">We have an exceptionally high</div><div class="stars"><svg width="60" height="9"><g fill="#ffc214"><use href="#s"/><use href="#s" x="12.5"/><use href="#s" x="25"/></g><g fill="#fff"><use href="#s" x="37.5"/><use href="#s" x="50"/></g></svg></div></div></div>
    <div class="story"><div class="story-photo" role="img" aria-label="Client photo"></div><div><div class="story-name">Martin Hollowbrook</div><div class="story-text">We have an exceptionally high</div><div class="stars"><svg width="60" height="9"><g fill="#ffc214"><use href="#s"/><use href="#s" x="12.5"/><use href="#s" x="25"/></g><g fill="#fff"><use href="#s" x="37.5"/><use href="#s" x="50"/></g></svg></div></div></div>
    <div class="story"><div class="story-photo" role="img" aria-label="Client photo"></div><div><div class="story-name">Martin Hollowbrook</div><div class="story-text">We have an exceptionally high</div><div class="stars"><svg width="60" height="9"><g fill="#ffc214"><use href="#s"/><use href="#s" x="12.5"/><use href="#s" x="25"/></g><g fill="#fff"><use href="#s" x="37.5"/><use href="#s" x="50"/></g></svg></div></div></div>
    <div class="story"><div class="story-photo" role="img" aria-label="Client photo"></div><div><div class="story-name">Martin Hollowbrook</div><div class="story-text">We have an exceptionally high</div><div class="stars"><svg width="60" height="9"><g fill="#ffc214"><use href="#s"/><use href="#s" x="12.5"/><use href="#s" x="25"/></g><g fill="#fff"><use href="#s" x="37.5"/><use href="#s" x="50"/></g></svg></div></div></div>
    <div class="story"><div class="story-photo" role="img" aria-label="Client photo"></div><div><div class="story-name">Martin Hollowbrook</div><div class="story-text">We have an exceptionally high</div><div class="stars"><svg width="60" height="9"><g fill="#ffc214"><use href="#s"/><use href="#s" x="12.5"/><use href="#s" x="25"/></g><g fill="#fff"><use href="#s" x="37.5"/><use href="#s" x="50"/></g></svg></div></div></div>
    <div class="story"><div class="story-photo" role="img" aria-label="Client photo"></div><div><div class="story-name">Martin Hollowbrook</div><div class="story-text">We have an exceptionally high</div><div class="stars"><svg width="60" height="9"><g fill="#ffc214"><use href="#s"/><use href="#s" x="12.5"/><use href="#s" x="25"/></g><g fill="#fff"><use href="#s" x="37.5"/><use href="#s" x="50"/></g></svg></div></div></div>
    <div class="story"><div class="story-photo" role="img" aria-label="Client photo"></div><div><div class="story-name">Martin Hollowbrook</div><div class="story-text">We have an exceptionally high</div><div class="stars"><svg width="60" height="9"><g fill="#ffc214"><use href="#s"/><use href="#s" x="12.5"/><use href="#s" x="25"/></g><g fill="#fff"><use href="#s" x="37.5"/><use href="#s" x="50"/></g></svg></div></div></div>
    <div class="story"><div class="story-photo" role="img" aria-label="Client photo"></div><div><div class="story-name">Martin Hollowbrook</div><div class="story-text">We have an exceptionally high</div><div class="stars"><svg width="60" height="9"><g fill="#ffc214"><use href="#s"/><use href="#s" x="12.5"/><use href="#s" x="25"/></g><g fill="#fff"><use href="#s" x="37.5"/><use href="#s" x="50"/></g></svg></div></div></div>
    <div class="story"><div class="story-photo" role="img" aria-label="Client photo"></div><div><div class="story-name">Martin Hollowbrook</div><div class="story-text">We have an exceptionally high</div><div class="stars"><svg width="60" height="9"><g fill="#ffc214"><use href="#s"/><use href="#s" x="12.5"/><use href="#s" x="25"/></g><g fill="#fff"><use href="#s" x="37.5"/><use href="#s" x="50"/></g></svg></div></div></div>
  </div>

  <div class="offers abs">
    <a class="offer" href="https://bookwell.example/brightorbitcoaching">
      <svg width="24" height="24" viewBox="0 0 24 24" fill="none" stroke="#1f2124" stroke-width="1.5"><circle cx="9" cy="5" r="3"/><path d="M4 22v-8a5 5 0 0 1 10 0v8M2 22h20M14 13l7-6"/></svg>
      PERSONAL COACHING / MENTORING
      <svg class="chev" width="60" height="38"><path d="M10 0h14l18 19-18 19H10l18-19z M30 0h14l16 19-16 19H30l18-19z" fill="#ffe27a" opacity=".7"/></svg>
    </a>
    <a class="offer" href="#">
      <svg width="24" height="24" viewBox="0 0 24 24" fill="none" stroke="#1f2124" stroke-width="1.5"><rect x="2" y="4" width="18" height="17" rx="1"/><path d="M2 9h18M7 2v4M15 2v4"/><circle cx="19" cy="19" r="3.5" fill="#1f2124"/></svg>
      HUMAN BEHAVIOUR EVENTS
      <svg class="chev" width="60" height="38"><path d="M10 0h14l18 19-18 19H10l18-19z M30 0h14l16 19-16 19H30l18-19z" fill="#ffe27a" opacity=".7"/></svg>
    </a>
    <a class="offer" href="#">
      <svg width="24" height="24" viewBox="0 0 24 24" fill="none" stroke="#1f2124" stroke-width="1.5"><circle cx="12" cy="7" r="5"/><path d="M3 22a9 7 0 0 1 18 0z"/></svg>
      GUEST SPEAKER
      <svg class="chev" width="60" height="38"><path d="M10 0h14l18 19-18 19H10l18-19z M30 0h14l16 19-16 19H30l18-19z" fill="#ffe27a" opacity=".7"/></svg>
    </a>
    <a class="offer" href="#">
      <svg width="24" height="24" viewBox="0 0 24 24" fill="none" stroke="#1f2124" stroke-width="1.5"><circle cx="10" cy="6" r="4"/><path d="M2 22v-5a8 6 0 0 1 16 0v5M15 15l6 6"/></svg>
      GREAT VALUE PRODUCTS
      <svg class="chev" width="60" height="38"><path d="M10 0h14l18 19-18 19H10l18-19z M30 0h14l16 19-16 19H30l18-19z" fill="#ffe27a" opacity=".7"/></svg>
    </a>
    <a class="offer" href="#">
      <svg width="24" height="24" viewBox="0 0 24 24" fill="none" stroke="#1f2124" stroke-width="1.5"><circle cx="12" cy="12" r="10.5"/><circle cx="12" cy="6.5" r="1.5"/><path d="M12 10v9M9.5 19h5"/></svg>
      GREAT FREE INFORMATION
      <svg class="chev" width="60" height="38"><path d="M10 0h14l18 19-18 19H10l18-19z M30 0h14l16 19-16 19H30l18-19z" fill="#ffe27a" opacity=".7"/></svg>
    </a>
  </div>
</section>

<footer class="site-footer abs">
  <p class="copyright">Copyright © 2017 Bright Orbit Coaching. All rights reserved.</p>
</footer>

</body>
</html>
```